Business card for Full Stable Care Vandorpe

I would like to have me designed an professional business card with my existing logo for my company called : full stable care vandorpe gcv.
I prefer a two sided business card with on the back side only the horses head and the website : fscvandorpe-example.eu
Only one colour shouldbe all right.
The logo must appear in a nic professional way on the business card.

Other suggestion are welcome.

All copy wrights must be released by the designer after we have selected a final design.

Target Market(s)

Equestrian businesses

Industry/Entity Type

Business

Contact Information for Business Card

Laurent Vandorpe
Title: zaakvoerder
Full Stable Care Vandorpe GCV
Molkenweg 47
B - 2820 Bonheiden
België
Phone: + 32 491 68 27 04
Mail: laurent@fscvandorpe-example.eu

Font styles to use
Serif

Requirements
Must have
• My own logo
• See attached files
• Website: fscvandorpe-example.eu

```html
<!DOCTYPE html>
<html lang="nl">
<head>
<meta charset="utf-8">
<title>Full Stable Care Vandorpe GCV – visitekaartje</title>
<link rel="stylesheet" href="https://fonts.googleapis.com/css2?family=Tinos:wght@700&family=Signika:wght@400&display=swap">
<style>
  :root {
    --backdrop: #4b4f56;
    --card-white: #ffffff;
    --card-black: #1c1a1b;
    --ink: #1a1a1a;
    --ink-soft: #4a4a4a;
    --rule: #8a8a8a;
    --on-dark: #ffffff;
    --on-dark-rule: #6d6d6d;
  }
  * { box-sizing: border-box; margin: 0; padding: 0; }
  html, body {
    width: 1200px; height: 1200px; overflow: hidden;
    background: var(--backdrop);
  }
  .canvas {
    width: 1200px; height: 1200px;
    display: flex; flex-direction: column; align-items: center; justify-content: center;
    gap: 36px;
  }
  .card {
    width: 900px; height: 514px; position: relative; overflow: hidden;
  }

  /* Back side */
  .card--back {
    background: var(--card-black);
    display: flex; flex-direction: column; align-items: center; justify-content: center;
  }
  .back__name {
    font-family: "Tinos", "Times New Roman", serif; font-weight: 700;
    color: var(--on-dark); font-size: 40px; letter-spacing: 1px;
    display: flex; align-items: center; gap: 18px;
  }
  .back__mark {
    width: 22px; height: 22px; border-radius: 50%; background: var(--on-dark);
  }
  .back__rule {
    width: 380px; height: 1px; margin: 34px 0 26px;
    background: linear-gradient(90deg, transparent, var(--on-dark-rule), transparent);
  }
  .back__web {
    font-family: "Signika", Arial, sans-serif; color: var(--on-dark);
    font-size: 34px; letter-spacing: 1.5px;
  }

  /* Front side */
  .card--front { background: var(--card-white); }
  .front__brand {
    position: absolute; left: 66px; top: 74px;
    font-family: "Tinos", "Times New Roman", serif; font-weight: 700;
    color: var(--ink); font-size: 36px; line-height: 1.05;
    display: flex; align-items: center; gap: 16px;
  }
  .front__mark { width: 20px; height: 20px; border-radius: 50%; background: var(--ink); flex: none; }
  .front__details {
    position: absolute; right: 60px; top: 202px; width: 370px;
    text-align: right; font-family: "Signika", Arial, sans-serif; color: var(--ink-soft);
  }
  .person__name {
    font-family: "Tinos", "Times New Roman", serif; font-weight: 700;
    color: var(--ink); font-size: 28px; letter-spacing: 0.5px; text-transform: uppercase;
  }
  .person__role { font-size: 22px; margin-top: 6px; }
  .dotted-rule { border-top: 2px dotted var(--rule); margin: 14px 0 12px; }
  .contact p, .address p { font-size: 22px; line-height: 1.45; }
  .address p + p { margin-top: 8px; }
</style>
</head>
<body>
<main class="canvas">
  <section class="card card--back" aria-label="Achterzijde">
    <div class="back__name"><span class="back__mark"></span>Full Stable Care Vandorpe</div>
    <div class="back__rule"></div>
    <div class="back__web">www.fscvandorpe-example.eu</div>
  </section>

  <section class="card card--front" aria-label="Voorzijde">
    <div class="front__brand"><span class="front__mark"></span><span>Full Stable Care<br>Vandorpe GCV</span></div>
    <div class="front__details">
      <h1 class="person__name">Laurent Vandorpe</h1>
      <p class="person__role">zaakvoerder</p>
      <div class="dotted-rule"></div>
      <div class="contact">
        <p>+ 32 491 68 27 04</p>
        <p>fscvandorpe-example.eu</p>
        <p>laurent@fscvandorpe-example.eu</p>
      </div>
      <div class="dotted-rule"></div>
      <div class="address">
        <p>Molkenweg 47</p>
        <p>B - 2870 Lindeveld, Vlaanderen</p>
      </div>
    </div>
  </section>
</main>
</body>
</html>
```